Global Careers Business Needs a Flyer Design

We need a flyer design to promote our Open Path Talks seminars.
We provide free career tools and insights to young professionals through our business Bright Harbour.

We would like to see our corporate colours utilised in the flyer
Grey R66 G73 B74
Teal R38 G128 B138
White R242 G240 B230

Attached is the flyer content, logo of our business and the image we wish to be used. Please note we would like to see two options of the image reflected in our teal corporate colour and a black and white option.

The final design should communicate a professional, eye-catching finish with a layout that captures the attention of our online users. Open to portrait or landscape layout.
Updates

Please note I will also require a JPEG file as well as the PDF for this piece of work. Added Friday, June 26, 2015

Target Market(s)

20-30's

Industry/Entity Type

Business

Font styles to use
Serif
Sans Serif
Other font styles liked:
• Calibri, Helvetica

Requirements
Must have
• Logo
• a DESIGN element -I do not wish to see the content just pasted onto the image. Please consider a design element, font styles, colours, etc
Nice to have
• Consider highlighting the quote by Helen Maddox.
Should not have
• I do not wish to see the content just pasted onto the image. Please consider a design element, font styles, colours, etc

```html
<!DOCTYPE html>
<html lang="en">
<head>
<meta charset="utf-8">
<title>Open Path Talks – Bright Harbour Seminar Flyer</title>
<link rel="stylesheet" href="https://fonts.googleapis.com/css2?family=Arimo:wght@400;700&family=Montserrat:wght@400;500&family=Lora:ital@1&display=swap">
<style>
  :root {
    --brand-grey: #42494a;
    --brand-teal: #26808a;
    --brand-white: #f2f0e6;
    --hero-grey-light: #b9bbbb;
    --hero-grey-dark: #7d8081;
    --hero-teal-light: #6fc3cc;
    --hero-teal-dark: #2f8e99;
    --quote-band: #5b5e5f;
    --body-text: #4a4d4e;
  }
  * { box-sizing: border-box; margin: 0; padding: 0; }
  html, body { width: 900px; height: 1200px; overflow: hidden; background: var(--brand-white); }
  .flyer { position: relative; width: 900px; height: 1200px; background: var(--brand-white); font-family: "Arimo", Arial, sans-serif; }

  .hero { position: absolute; left: 0; top: 0; width: 900px; height: 511px; }
  .hero-photo { position: absolute; inset: 0;
    background: linear-gradient(180deg, var(--hero-grey-dark) 0%, var(--hero-grey-light) 60.6%, var(--hero-teal-dark) 60.6%, var(--hero-teal-light) 100%); }

  .brand-dot { position: absolute; left: 36px; top: 112px; width: 60px; height: 60px; border: 3px solid var(--brand-white); border-radius: 50%; }
  .brand-name { position: absolute; left: 147px; top: 90px; font-family: "Montserrat", Arial, sans-serif; font-weight: 500; color: var(--brand-white);
    font-size: 52px; line-height: 62px; letter-spacing: 6px; text-transform: uppercase; }
  .tagline { position: absolute; left: 149px; top: 217px; font-family: "Montserrat", Arial, sans-serif; font-weight: 400;
    color: var(--brand-white); font-size: 14px; letter-spacing: 3px; text-transform: uppercase; }

  .quote-band { position: absolute; left: 0; top: 511px; width: 900px; height: 66px; background: var(--quote-band);
    display: flex; align-items: center; justify-content: center; text-align: center; padding: 0 40px; }
  .quote-band p { font-family: "Lora", Georgia, serif; font-style: italic; color: var(--brand-white); font-size: 18px; line-height: 25px; letter-spacing: 0.3px; }
  .quote-band .quote-author { color: var(--brand-teal); }

  .content { position: absolute; left: 0; top: 577px; width: 900px; height: 514px; }
  .column-left { position: absolute; left: 38px; top: 46px; width: 350px; }
  .column-divider { position: absolute; left: 459px; top: 103px; width: 2px; height: 343px; background: var(--brand-teal); }
  .column-right { position: absolute; left: 505px; top: 46px; width: 390px; }

  .section-title { color: var(--brand-teal); font-weight: 700; text-transform: uppercase; }
  .column-left .section-title { font-size: 32px; line-height: 38px; margin-bottom: 27px; }
  .column-right .section-title { font-size: 29px; line-height: 38px; margin-bottom: 36px; white-space: nowrap; }

  .intro p { color: var(--body-text); font-weight: 700; font-size: 13.4px; line-height: 17px; text-align: justify; margin-bottom: 17px; }

  .outcomes { list-style: none; width: 365px; }
  .outcomes li { position: relative; padding-left: 17px; color: var(--brand-grey); font-weight: 700; font-size: 24px; line-height: 30px; margin-bottom: 2px; }
  .outcomes li::before { content: ""; position: absolute; left: 0; top: 10px; width: 10px; height: 10px; background: var(--brand-teal); }

  .audience-band { position: absolute; left: 0; top: 1091px; width: 900px; height: 109px; background: var(--brand-teal);
    display: flex; justify-content: center; padding-top: 26px; }
  .audience-band p { color: var(--brand-white); font-weight: 700; font-size: 16px; line-height: 20px; text-align: center; text-transform: uppercase; max-width: 700px; }
</style>
</head>
<body>
<main class="flyer">
  <header class="hero">
    <div class="hero-photo" role="img" aria-label="Rollercoaster track climbing against a cloudy sky, black and white above and tinted teal below"></div>
    <div class="brand-dot"></div>
    <h1 class="brand-name">Bright<br>Harbour</h1>
    <p class="tagline">Careers with direction</p>
  </header>

  <section class="quote-band">
    <p>“Young people need to view their career as the equivalent of a rollercoaster ride but believe they can control the dips and turns.” -<span class="quote-author">Helen Maddox</span></p>
  </section>

  <section class="content">
    <div class="column-left">
      <h2 class="section-title">Open Path Talks</h2>
      <div class="intro">
        <p>Making the transition from school or university to work is no small step. In fact studies show that young people require considerable support during this early stage to ensure their employment is sustained.</p>
        <p>With the average person spending over 90,000 hours of their life at work, and changing jobs seven to eight times before thirty - It’s critical to prepare.</p>
        <p>Open Path Talks is a high energy seminar that addresses key elements, often lost and forgotten in the lead up to entering the workforce.</p>
        <p>Helen Maddox, a passionate and outspoken former career banker turned entrepreneur delivers a message with conviction. “Young people need to view their career as the equivalent of a rollercoaster ride but believe they can control the dips and turns.”</p>
      </div>
    </div>
    <div class="column-divider"></div>
    <div class="column-right">
      <h2 class="section-title">Open Path Talks will<br>explore how to:</h2>
      <ul class="outcomes">
        <li>Overcome setbacks at work</li>
        <li>Influence what people say about you</li>
        <li>Embrace both good and not so good feedback</li>
        <li>Start building a success story for your future</li>
      </ul>
    </div>
  </section>

  <footer class="audience-band">
    <p>This seminar is ideal for high school leavers, college graduates and developing young professionals.</p>
  </footer>
</main>
</body>
</html>
```